Packaging designed for both the bar and the box for retail and online sales

The name of the product is Plume Crumb. We manufacture a consumer package good product that's a healthy edible cookie dough bar. The product look, feels and tastes like cookie dough. It's sold in the refrigerator section of retail stores next to cookie dough and tundra loaf. The product is Gluten Free, Diary Free and include B-12, Biotin and Collagen. The ingredients are natural. When design this think about who eat cookie dough and how to engage the buyer in purchasing the product.

We needs design packaging designed for both the bar and the box. I have attached the die lines for both products.

Target Market(s)

Our customer is 16-45. Primarily female but really anyone. Middle to upper income. Interest include healthy life style and yoga. Like to eat something sweet but not feel guilty.

Colors

Designer to choose colors to be used in the design.

Requirements
Must have
• Must be clean, warm, inviting. Brand designs I really like are Tundra Loaf.
Should not have
• Should not have a photo of food

```html
<!DOCTYPE html>
<html lang="en">
<head>
<meta charset="utf-8">
<title>Plume Crumb – Bar Wrapper</title>
<link rel="stylesheet" href="https://fonts.googleapis.com/css2?family=Roboto+Condensed:wght@700&family=Arimo:wght@400&display=swap">
<style>
  :root {
    --backdrop: #9ca6aa;
    --wrapper-white: #f4f4f4;
    --crimp-line: #d6d6d6;
    --gold: #e9b32a;
    --gold-deep: #d99e18;
    --gold-stripe: #f0b52a;
    --brand-brown: #9a6a12;
    --claim-brown: #5a2a0e;
    --leaf-green: #2e9a1c;
    --leaf-light: #b9e8a6;
    --copy-ink: #2b2b2b;
  }
  * { box-sizing: border-box; margin: 0; padding: 0; }
  html, body { width: 1200px; height: 614px; overflow: hidden; }
  body { background: var(--backdrop); position: relative; font-family: "Arimo", Arial, sans-serif; }

  .wrapper {
    position: absolute;
    width: 607px;
    height: 225px;
    background: var(--wrapper-white);
    overflow: hidden;
  }
  .wrapper--front { left: 81px; top: 56px; }
  .wrapper--back { left: 471px; top: 315px; }

  .crimp {
    position: absolute;
    top: 0;
    width: 16px;
    height: 100%;
    background: repeating-linear-gradient(90deg, rgba(255,255,255,.45) 0 2px, rgba(0,0,0,.08) 2px 4px);
  }
  .crimp--left { left: 0; }
  .crimp--right { right: 0; }

  .pattern-panel {
    position: absolute;
    top: 0;
    height: 100%;
    background: linear-gradient(180deg, var(--gold) 0%, var(--gold-deep) 100%);
  }
  .wrapper--front .pattern-panel { left: 0; width: 289px; }
  .wrapper--back .pattern-panel { left: 324px; width: 283px; }

  .gold-stripe {
    position: absolute;
    top: 0;
    width: 10px;
    height: 100%;
    background: var(--gold-stripe);
  }
  .wrapper--front .gold-stripe { left: 301px; }
  .wrapper--back .gold-stripe { left: 299px; }

  .claims {
    position: absolute;
    left: 55px;
    top: 134px;
    font-family: "Roboto Condensed", "Arial Narrow", sans-serif;
    font-weight: 700;
    font-size: 14px;
    line-height: 17px;
    color: var(--claim-brown);
  }

  .brand-name {
    position: absolute;
    left: 318px;
    top: 88px;
    width: 250px;
    text-align: center;
    font-family: "Roboto Condensed", "Arial Narrow", sans-serif;
    font-weight: 700;
    font-size: 50px;
    line-height: 54px;
    color: var(--brand-brown);
  }

  .natural-badge {
    position: absolute;
    left: 461px;
    top: -82px;
    width: 170px;
    height: 170px;
    border-radius: 50%;
    background: var(--leaf-green);
  }
  .natural-badge__text {
    position: absolute;
    left: 483px;
    top: 18px;
    transform: rotate(-45deg);
    transform-origin: center;
    font-family: "Roboto Condensed", "Arial Narrow", sans-serif;
    text-align: center;
    line-height: 1;
  }
  .natural-badge__percent { display: block; font-weight: 700; font-size: 22px; color: #fff; }
  .natural-badge__word { display: block; font-size: 16px; color: var(--leaf-light); }

  .ingredient-copy {
    position: absolute;
    left: 62px;
    top: 20px;
    height: 188px;
    writing-mode: vertical-rl;
    transform: rotate(180deg);
    font-size: 13.5px;
    line-height: 18.6px;
    color: var(--copy-ink);
  }
</style>
</head>
<body>

  <section class="wrapper wrapper--front" aria-label="Plume Crumb bar wrapper, front">
    <div class="pattern-panel" role="img" aria-label="Golden swirl pattern panel"></div>
    <div class="crimp crimp--left"></div>
    <div class="crimp crimp--right"></div>
    <div class="gold-stripe"></div>
    <p class="claims">Gluten Free,<br>Diary Free<br>Include B-12, Biotin and Collagen.</p>
    <h1 class="brand-name">Plume<br>Crumb</h1>
    <div class="natural-badge"></div>
    <p class="natural-badge__text">
      <span class="natural-badge__percent">100%</span>
      <span class="natural-badge__word">Natural</span>
    </p>
  </section>

  <section class="wrapper wrapper--back" aria-label="Plume Crumb bar wrapper, back">
    <div class="pattern-panel" role="img" aria-label="Golden swirl pattern panel"></div>
    <div class="crimp crimp--left"></div>
    <div class="crimp crimp--right"></div>
    <div class="gold-stripe"></div>
    <p class="ingredient-copy">Lorem ipsum dolor sit amet,<br>consectetur adipiscing elit.<br>Phasellus eu risus tincidunt,<br>tempus lacus et, malesuada<br>sem. Nunc fermentum porta<br>egestas. Praesent id risus<br>non erat lacinia laoreet. Nulla<br>eu nulla urna. Suspendisse<br>convallis, arcu at dignissim<br>laoreet, velit tellus consequat<br>mauris, non lacinia lectus<br>urna a diam.</p>
  </section>

</body>
</html>
```